Business Card template designs

We need a lot of Business card designs.
Your designs will get exposure on our newly opened business-card printing website.
We are committed to quality of paper and packages we use, so they will come up very fancy.

Here is your advantage. We will put the profile of the graphic designer on our site so that you can showcase your designs to people around the world and in Japan.

A profile is not mandatory, although we encourage graphic designers to have a profile to get continuous work in the future.
We are looking forward to having many good designs.

The right of the use of design will be owned by us.
The design may be used to the products other than
business cards.

Target Market(s)

designer,photographer,creator,artist

Industry/Entity Type

Printing

Contact Information for Business Card

The back design is important.
Please check the reference file.

Requirements
Must have
• Please include the following, required information on your business card designs.
• Name: Haruna Okabe
• Title: Designer
• Web: https://www.ketori.co.jp/kt/
• Address: 4-17 Kamiharuta-Cho Meguro-ku, Tokyo
• Email: info@kketori.com
• Phone: 03 4816 3907
• Mobile: 070 2143 6658
• * For Japanese sites, we will convert the text portion to Japanese characters.
• * In case of 28mmx70mm only include Name,Enail,Phone and SNS account(https://www.facebook.com/kketori.com)
• 1. colorful
• 2. simple
• 3. natural
• 4. modern
• 5. cool
• 6. sporty
• Please make variations of the same image with 3-6
• different colors / patterns for one design so that
• customers can compare and choose.
• If you want to use a same picture, please make make
• copies and paste on each different types of design.
Nice to have
• You may also use, the following non-required information.
• Company Name: Ketori, Inc.
• Fax: 03-4173-9620
• Open space for company logo

```html
<!DOCTYPE html>
<html lang="en">
<head>
<meta charset="utf-8">
<title>Business Card – Front and Back</title>
<link rel="stylesheet" href="https://fonts.googleapis.com/css2?family=Marcellus&family=Montserrat:wght@600&family=Lato:wght@400;700&display=swap">
<style>
  :root {
    --backdrop: #333333;
    --backdrop-edge: #2b2b2b;
    --paper: #ffffff;
    --brand-red: #a4210d;
    --ink: #222222;
    --muted-light: #e6c9c2;
  }
  * { margin: 0; padding: 0; box-sizing: border-box; }
  html, body { width: 1200px; height: 900px; overflow: hidden; }
  body {
    position: relative;
    background: radial-gradient(ellipse at center, var(--backdrop) 0%, var(--backdrop-edge) 100%);
    font-family: "Lato", sans-serif;
  }
  .card {
    position: absolute;
    top: 170px;
    width: 347px;
    height: 561px;
    text-align: center;
  }
  .card--front { left: 259px; background: var(--paper); }
  .card--back { left: 631px; background: var(--brand-red); }

  .logo-placeholder {
    position: absolute;
    left: 0; right: 0;
    font-family: "Marcellus", serif;
    line-height: 0.86;
    letter-spacing: -1px;
  }
  .card--front .logo-placeholder {
    top: 82px;
    font-size: 80px;
    color: var(--brand-red);
  }
  .card--back .logo-placeholder {
    top: 197px;
    font-size: 86px;
    color: var(--paper);
  }

  .contact {
    position: absolute;
    left: 0; right: 0;
    top: 347px;
    color: var(--ink);
    font-size: 15px;
  }
  .contact__name {
    font-family: "Montserrat", sans-serif;
    font-weight: 600;
    font-size: 22px;
    color: var(--brand-red);
    line-height: 1.2;
  }
  .contact__title { font-size: 14px; line-height: 1.2; margin-bottom: 13px; }
  .contact__lines { list-style: none; line-height: 21px; margin-bottom: 7px; }
  .contact__label { font-weight: 700; color: var(--brand-red); }
  .contact__address { font-style: normal; line-height: 20px; }

  .card__web {
    position: absolute;
    left: 0; right: 0;
    top: 484px;
    font-size: 18px;
    font-weight: 700;
    color: var(--muted-light);
  }
</style>
</head>
<body>
  <section class="card card--front">
    <div class="logo-placeholder">Logo<br>Here</div>
    <div class="contact">
      <h1 class="contact__name">Haruna Okabe</h1>
      <p class="contact__title">Designer</p>
      <ul class="contact__lines">
        <li><span class="contact__label">P:</span> 03 4816 3907</li>
        <li><span class="contact__label">M:</span> 070 2143 6658</li>
        <li><span class="contact__label">E:</span> info@kketori.com</li>
      </ul>
      <address class="contact__address">4-17 Kamiharuta-Cho<br>Meguro-ku, Tokyo</address>
    </div>
  </section>

  <section class="card card--back">
    <div class="logo-placeholder">Logo<br>Here</div>
    <p class="card__web">www.ketori.co.jp/kt/</p>
  </section>
</body>
</html>
```